Bright Sprout Learning Centre website redesign

Our website (which we have only just converted to wordpress) is just not good enough for my liking. Our centre offers classes for babies aged from 6 months to 7 years old in the middle east. Whilst our program is formal in the way that the practise deals with learning in hemispheres of the brain - the site should look more fun and a bit more approachable and attractive to families.
I like the site www.tallowpine.com or www.corvidlane.com from this region - I like the way that you land on home page with images and a quote rather than all this information coming at you and you not knowing where to click.
I want a fun and appealing site that features info about the program, class timetable, shop, news and events, gallery, blog posts etc…
I am really open to a complete redesign and just want something that looks professional but is fun and gets the information out quickly! Please look at www.brightsprout.ae for current site design

```html
<!DOCTYPE html>
<html lang="en">
<head>
<meta charset="utf-8">
<title>Bright Sprout Learning Centre</title>
<link href="https://fonts.googleapis.com/css2?family=Roboto:wght@400;500;700&family=Open+Sans:wght@400;600&display=swap" rel="stylesheet">
<style>
:root{
  --brand:#4a8bab;
  --brand-dark:#1f6f95;
  --brand-tint:#c9dde7;
  --green:#8dc124;
  --pink:#ef1aa5;
  --purple:#7750be;
  --nav:#8a8a8a;
  --social:#7d7d7d;
  --text:#555;
  --quote:#444;
  --white:#fff;
}
*{margin:0;padding:0;box-sizing:border-box}
html,body{width:1046px;height:1200px;overflow:hidden;background:var(--white)}
body{position:relative;font-family:'Roboto',sans-serif;color:var(--text)}
.abs{position:absolute}

.brand{left:151px;top:14px;width:88px;height:106px;display:flex;flex-direction:column;align-items:center;justify-content:flex-end;gap:6px}
.brand-mark{width:44px;height:44px;border-radius:50%;background:var(--brand)}
.brand-name{font-weight:700;font-size:12px;color:var(--brand);text-align:center;line-height:1.15}

.social{left:640px;top:30px;display:flex;gap:8px}
.social span{width:27px;height:27px;border-radius:50%;background:var(--social);display:block}
.contact-btn{left:835px;top:30px;width:62px;height:27px;border:1.5px solid var(--brand);border-radius:14px;color:var(--brand);font-size:13px;display:flex;align-items:center;justify-content:center}

.main-nav{left:311px;top:99px;display:flex;gap:31px;font-size:15.5px;letter-spacing:.6px;color:var(--nav)}

.hero{left:150px;top:130px;width:747px;height:288px;background:linear-gradient(100deg,#d9c2b0 0%,#e8e6e2 30%,#c9392f 32%,#c9392f 45%,#ecebe7 48%,#e9b27a 60%,#a78a6f 78%,#6c6d70 100%)}
.hero-caption{left:150px;top:386px;width:747px;height:32px;background:rgba(74,139,171,.85);color:var(--white);font-family:'Open Sans',sans-serif;font-size:13.4px;padding:6px 20px}
.hero-arrow{width:56px;height:56px;border-radius:50%;background:var(--brand);border:3px solid var(--white);top:246px;display:flex;align-items:center;justify-content:center}
.hero-arrow.prev{left:115px}
.hero-arrow.next{left:871px}

.tiles{left:150px;top:434px;display:flex;gap:21px}
.tile{width:171px;height:112px;border-radius:8px;color:var(--white);font-size:9.5px;font-weight:700;display:flex;flex-direction:column;align-items:center;justify-content:flex-end;padding-bottom:17px;gap:10px}
.tile svg{width:52px;height:52px}
.tile.timetable{background:var(--green)}
.tile.program{background:var(--brand)}
.tile.about{background:var(--pink)}
.tile.location{background:var(--purple)}

.section-title{left:150px;top:583px;font-size:15px;font-weight:700;color:var(--brand)}
.featured-arrows{left:860px;top:580px}
.featured{left:150px;top:617px;display:flex;gap:20px}
.featured div{width:171px;height:113px}
.f1{background:linear-gradient(135deg,#2f5d64,#d2c4b4 60%,#3c4d7a)}
.f2{background:linear-gradient(135deg,#7a6e60,#d8b39a 50%,#254d7a)}
.f3{background:linear-gradient(180deg,#6b9b3c,#c8322a 60%,#b22a22)}
.f4{background:linear-gradient(135deg,#c7d0c0,#b88a74 50%,#e6a5b7)}

.quote{left:253px;top:782px;font-family:'Open Sans',sans-serif;font-size:16.5px;color:var(--quote);line-height:1.3}
.quote cite{display:block;font-style:normal;color:var(--brand-dark)}

.col-head{top:890px;height:21px;background:var(--brand);color:var(--white);border-radius:6px;font-size:14px;padding:1px 12px}
.team-photo{left:150px;top:923px;width:218px;height:148px;background:linear-gradient(160deg,#efece9,#c9a58f 50%,#6e4b3a 75%,#e8e4e0)}
.team-caption{left:148px;top:1078px;font-size:10px;color:#222}
.press{left:383px;top:924px;width:265px;font-size:9.2px;line-height:12.6px;text-align:justify;color:#666}
.contact-info{left:664px;top:924px;font-size:9.5px;line-height:15.6px;color:#666;font-style:normal}

.skyline{left:160px;top:1092px;width:725px;height:68px;background:linear-gradient(180deg,var(--white) 0%,var(--brand-tint) 45%,var(--brand) 100%)}
.footer-band{left:0;top:1160px;width:1046px;height:40px;background:var(--brand)}
</style>
</head>
<body>

<div class="abs brand"><span class="brand-mark"></span><span class="brand-name">Bright Sprout</span></div>

<div class="abs social" aria-label="Social links"><span></span><span></span><span></span><span></span><span></span></div>
<div class="abs contact-btn">Contact</div>

<nav class="abs main-nav"><span>Home</span><span>The Program</span><span>Classes</span><span>Media</span><span>Blog</span><span>About us</span><span>Shop</span></nav>

<div class="abs hero" role="img" aria-label="Photo of teachers playing with a smiling baby in a bright classroom"></div>
<div class="abs hero-caption">Our accelerated learning classes, taught in English, are for children aged from 6 months old.</div>
<div class="abs hero-arrow prev"><svg width="20" height="22" viewBox="0 0 20 22"><path d="M13 3 L5 11 L13 19" stroke="#fff" stroke-width="4" fill="none"/></svg></div>
<div class="abs hero-arrow next"><svg width="20" height="22" viewBox="0 0 20 22"><path d="M7 3 L15 11 L7 19" stroke="#fff" stroke-width="4" fill="none"/></svg></div>

<div class="abs tiles">
  <div class="tile timetable"><svg viewBox="0 0 52 52"><circle cx="26" cy="26" r="23" fill="#fff"/><path d="M26 12 V28 H16" stroke="#8dc124" stroke-width="3" fill="none"/></svg>CLASS TIME TABLE</div>
  <div class="tile program"><svg viewBox="0 0 52 52"><rect x="3" y="5" width="46" height="32" rx="3" stroke="#fff" stroke-width="3" fill="none"/><path d="M26 37 V44 M16 46 H36" stroke="#fff" stroke-width="3"/></svg>THE PROGRAM</div>
  <div class="tile about"><svg viewBox="0 0 52 52"><path d="M36 4 L47 15 L17 45 L5 48 L8 36 Z" fill="#fff"/><path d="M31 9 L42 20" stroke="#ef1aa5" stroke-width="2"/></svg>ABOUT BRIGHT SPROUT</div>
  <div class="tile location"><svg viewBox="0 0 52 52"><path d="M13 40 H40 A9 9 0 0 0 40 22 A13 13 0 0 0 16 19 A10.5 10.5 0 0 0 13 40 Z" stroke="#fff" stroke-width="3" fill="none"/></svg>LOCATION</div>
</div>

<h2 class="abs section-title">Featured Program</h2>
<svg class="abs featured-arrows" width="36" height="24" viewBox="0 0 36 24"><path d="M13 3 L5 12 L13 21" stroke="#ddd" stroke-width="4" fill="none"/><path d="M23 3 L31 12 L23 21" stroke="#777" stroke-width="4" fill="none"/></svg>
<div class="abs featured">
  <div class="f1" role="img" aria-label="Photo of pupils writing at their desks"></div>
  <div class="f2" role="img" aria-label="Photo of a smiling boy in a classroom"></div>
  <div class="f3" role="img" aria-label="Photo of a child holding letter blocks outdoors"></div>
  <div class="f4" role="img" aria-label="Photo of a girl drawing in front of a world map"></div>
</div>

<blockquote class="abs quote">“Lorem ipsum dolor sit amet, consectetur adipiscing elit. Aeneanugiat,”<cite>---- Lorem ipsum</cite></blockquote>

<div class="abs col-head" style="left:150px;width:218px">Our Team</div>
<div class="abs col-head" style="left:383px;width:265px">Who’s talking about Bright Sprout?</div>
<div class="abs col-head" style="left:664px;width:218px">Contact Info</div>

<div class="abs team-photo" role="img" aria-label="Portrait photo of the centre founder"></div>
<p class="abs team-caption">Leila Haddad – Founder</p>

<p class="abs press">Lorem ipsum dolor sit amet, consectetur adipiscing elit. Aenean quis eros feugiat, pellentesque mauris vitae, eleifend diam. Aenean adipiscing leo lacus. Sed sit amet tortor eros. Morbi pellentesque orci sed pharetra rutrum. Integer eget nunc adipiscing, dignissim augue a, feugiat eros. Mauris at felis sit amet elit luctus rutrum. Quisque sed sollicitudin turpis, non consectetur magna.</p>

<address class="abs contact-info">G07, Block 4C<br>Harbor Learning Park<br>+971 45550192<br>register@brightsprout.ae</address>

<div class="abs skyline" role="img" aria-label="Illustration of a city skyline with clouds and a plane"></div>
<div class="abs footer-band"></div>

</body>
</html>
```